The Copperwell

We need a APP for our members. this is a Private Bar/Venue. history of the brick building is it was built in1898 and was a gentleman club, oyster house, cigar factory and then law offices before we purchased and are beginning restoration.
the APP must include
1. direct texting to the concierge
2. calendar of events
3. vantor Lock To open the lock, anyone with a code can approach the door, enable their phone's Bluetooth and press the relevant address from the app.
Read more: http://www.evenpostgazette.co.uk/sciencetech/article-4418206/farewell-metal-keys-phone-bolt-opens-front-door-without-anything-in-hand.html#ixzz9kQR2mpaL
4. Menus from various restaurants from our surrounding area
5. member name and member number to give the feel that the app is personalized
6. the members account balance
7. ability to pay their bill with credit card or quid line monthly and automatically.
8. link to züro with its own icon within the app.
9.the ability to reserve the room
Anything else that may of interest for our members that may be relevant that I may not have mentioned since we are new at this...
35 to 60 years of age
Club

```html
<!DOCTYPE html>
<html lang="en">
<head>
<meta charset="utf-8">
<title>The Copperwell — Calendar</title>
<link rel="stylesheet" href="https://fonts.googleapis.com/css2?family=Montserrat:wght@300;400;500;600&family=Questrial&display=swap">
<style>
  :root {
    --page: #e3e7ef;
    --black: #000;
    --panel: #141414;
    --time-panel: #1a1a1a;
    --bronze: #a88570;
    --white: #fff;
    --dim: #5a5a5a;
    --muted: #4a4a4a;
    --rule: #2a2a2a;
  }
  * { box-sizing: border-box; margin: 0; padding: 0; }
  html, body { width: 800px; height: 1200px; overflow: hidden; background: var(--page); }
  body { position: relative; font-family: "Montserrat", sans-serif; color: var(--white); }

  .app {
    position: absolute; left: 62.5px; top: 0;
    width: 750px; height: 1334px;
    transform: scale(0.9); transform-origin: 0 0;
    background: var(--black); overflow: hidden;
  }

  .status-bar { position: absolute; top: 0; left: 0; right: 0; height: 44px; font-size: 21px; font-weight: 300; }
  .status-bar .carrier { position: absolute; left: 14px; top: 7px; display: flex; align-items: center; gap: 6px; }
  .status-bar .clock { position: absolute; left: 0; right: 0; top: 7px; text-align: center; }
  .status-bar .battery { position: absolute; right: 14px; top: 7px; display: flex; align-items: center; gap: 6px; }

  .nav-header { position: absolute; top: 44px; left: 0; right: 0; height: 84px; }
  .nav-header .menu { position: absolute; left: 30px; top: 22px; }
  .nav-header .title {
    position: absolute; left: 0; right: 0; top: 26px; text-align: center;
    font-family: "Questrial", sans-serif; font-size: 27px; letter-spacing: 9px; padding-left: 9px;
  }

  .month-bar { position: absolute; top: 128px; left: 0; right: 0; height: 112px; background: var(--panel); }
  .month-bar .arrow { position: absolute; top: 38px; width: 40px; height: 40px; }
  .month-bar .prev { left: 148px; }
  .month-bar .next { left: 562px; }
  .month-bar .month { position: absolute; left: 0; right: 0; top: 36px; text-align: center; font-family: "Questrial", sans-serif; font-size: 36px; }

  .weekdays, .week { position: absolute; left: 30px; width: 690px; display: grid; grid-template-columns: repeat(7, 98.5px); text-align: center; }
  .weekdays { top: 272px; color: var(--bronze); font-size: 20px; font-weight: 300; }
  .week { height: 92px; font-family: "Questrial", sans-serif; font-size: 26px; }
  .day { position: relative; height: 92px; line-height: 92px; }
  .day.faded { color: var(--dim); }
  .day.event::before {
    content: ""; position: absolute; left: 50%; top: 6px; width: 9px; height: 9px; margin-left: -4.5px;
    border-radius: 50%; background: var(--white);
  }
  .day.faded.event::before { background: var(--dim); }
  .day.selected span {
    display: inline-block; width: 62px; height: 62px; line-height: 62px; border-radius: 50%;
    background: var(--bronze); vertical-align: middle;
  }

  .events { position: absolute; top: 800px; left: 0; right: 0; }
  .event-row { position: relative; height: 164px; }
  .event-row .time { position: absolute; left: 0; top: 0; width: 132px; height: 162px; background: var(--time-panel); padding: 14px 0 0 13px; font-size: 22px; font-weight: 300; line-height: 28px; }
  .event-row .photo { position: absolute; left: 132px; top: 0; width: 162px; height: 162px; }
  .event-row .info { position: absolute; left: 316px; right: 0; top: 0; height: 162px; border-bottom: 1px solid var(--rule); }
  .event-row .name { position: absolute; top: 44px; font-size: 31px; font-weight: 600; }
  .event-row .venue { position: absolute; top: 96px; font-size: 23px; font-weight: 300; color: var(--bronze); }

  .tab-bar { position: absolute; left: 0; right: 0; bottom: 0; height: 98px; background: var(--panel); display: grid; grid-template-columns: repeat(4, 1fr); }
  .tab { text-align: center; color: var(--muted); font-size: 18px; font-weight: 500; letter-spacing: 0.5px; padding-top: 16px; }
  .tab svg { display: block; margin: 0 auto 8px; height: 44px; }
  .tab.active { color: var(--white); }
</style>
</head>
<body>
<main class="app">
  <div class="status-bar">
    <div class="carrier">
      <svg width="68" height="12" viewBox="0 0 68 12"><g fill="#fff"><circle cx="6" cy="6" r="5"/><circle cx="19" cy="6" r="5"/><circle cx="32" cy="6" r="5"/></g><g fill="none" stroke="#fff" stroke-width="1.5"><circle cx="45" cy="6" r="4.3"/><circle cx="58" cy="6" r="4.3"/></g></svg>
      <span>Carrier</span>
      <svg width="24" height="18" viewBox="0 0 24 18"><g fill="none" stroke="#fff" stroke-width="2.4" stroke-linecap="round"><path d="M2 6a14 14 0 0 1 20 0"/><path d="M6 10a8 8 0 0 1 12 0"/></g><circle cx="12" cy="14.5" r="2.2" fill="#fff"/></svg>
    </div>
    <div class="clock">3:24 PM</div>
    <div class="battery"><span>100%</span>
      <svg width="48" height="20" viewBox="0 0 48 20"><rect x="1" y="1" width="43" height="18" rx="3" fill="none" stroke="#fff" stroke-width="1.5"/><rect x="3" y="3" width="39" height="14" rx="1.5" fill="#fff"/><rect x="45" y="7" width="2.5" height="6" fill="#fff"/></svg>
    </div>
  </div>

  <header class="nav-header">
    <svg class="menu" width="36" height="34" viewBox="0 0 36 34"><g fill="#fff"><rect y="0" width="36" height="3"/><rect y="15" width="36" height="3"/><rect y="30" width="36" height="3"/></g></svg>
    <h1 class="title">CALENDAR</h1>
  </header>

  <section class="month-bar">
    <svg class="arrow prev" viewBox="0 0 40 40"><circle cx="20" cy="20" r="20" fill="var(--bronze)"/><path d="M23 12l-8 8 8 8" fill="none" stroke="#000" stroke-width="3.2" stroke-linecap="round" stroke-linejoin="round"/></svg>
    <div class="month">May 2017</div>
    <svg class="arrow next" viewBox="0 0 40 40"><circle cx="20" cy="20" r="20" fill="var(--bronze)"/><path d="M17 12l8 8-8 8" fill="none" stroke="#000" stroke-width="3.2" stroke-linecap="round" stroke-linejoin="round"/></svg>
  </section>

  <div class="weekdays"><div>SUN</div><div>MON</div><div>TUE</div><div>WED</div><div>THU</div><div>FRI</div><div>SAT</div></div>

  <div class="week" style="top:309px"><div class="day faded">1</div><div class="day faded">2</div><div class="day faded">3</div><div class="day faded">4</div><div class="day faded">5</div><div class="day faded">6</div><div class="day faded">7</div></div>
  <div class="week" style="top:401px"><div class="day faded">8</div><div class="day selected"><span>9</span></div><div class="day">10</div><div class="day">11</div><div class="day">12</div><div class="day">13</div><div class="day">14</div></div>
  <div class="week" style="top:493px"><div class="day">15</div><div class="day event">16</div><div class="day">17</div><div class="day">18</div><div class="day">19</div><div class="day">20</div><div class="day">21</div></div>
  <div class="week" style="top:585px"><div class="day">22</div><div class="day event">23</div><div class="day">24</div><div class="day">25</div><div class="day">26</div><div class="day event">27</div><div class="day">28</div></div>
  <div class="week" style="top:677px"><div class="day">29</div><div class="day event">30</div><div class="day event">31</div><div class="day faded">1</div><div class="day faded event">2</div><div class="day faded event">3</div><div class="day faded">4</div></div>

  <section class="events">
    <article class="event-row">
      <div class="time">8:00 AM<br>–<br>9:00 AM</div>
      <div class="photo" role="img" aria-label="Black and white photo of a festive performer in a knit cap" style="background:linear-gradient(135deg,#8a8a8a,#3a3a3a 60%,#cfcfcf)"></div>
      <div class="info"><h2 class="name">Fiesta Fun</h2><p class="venue">The Back Room</p></div>
    </article>
    <article class="event-row">
      <div class="time">4:30 PM<br>–<br>6:00 PM</div>
      <div class="photo" role="img" aria-label="Candlelit table with glasses at an evening party" style="background:linear-gradient(160deg,#1c2f6e,#2a4fa0 45%,#7a4a2a 70%,#1a2550)"></div>
      <div class="info"><h2 class="name" style="left:-2px">Dance Wave!</h2><p class="venue" style="left:-2px">No Name Bar</p></div>
    </article>
    <article class="event-row">
      <div class="time">7:00 PM<br>–<br>8:00 PM</div>
      <div class="photo" role="img" aria-label="Crowded colorful party under festive lights" style="background:linear-gradient(180deg,#3a6a4a,#8a3a5a 40%,#c07a40 70%,#3a2a3a)"></div>
      <div class="info"><h2 class="name">80’s Pool Party</h2><p class="venue">Tempo Room</p></div>
    </article>
  </section>

  <nav class="tab-bar">
    <div class="tab">
      <svg viewBox="0 0 44 44" width="44"><g fill="none" stroke="currentColor" stroke-width="2"><path d="M6 4h14l-1 12a6 6 0 0 1-12 0z"/><path d="M13 22v18M8 40h10"/><path d="M26 4v12a4 4 0 0 0 8 0V4M30 4v36"/><path d="M38 4c4 4 4 14 0 16v20"/></g></svg>
      Restaurants
    </div>
    <div class="tab">
      <svg viewBox="0 0 44 44" width="44"><g fill="none" stroke="currentColor" stroke-width="2"><path d="M4 34h36M2 38h40M7 34a15 15 0 0 1 30 0M22 17v-3M18 14h8"/><path d="M22 4v4M11 8l2 3M33 8l-2 3"/></g></svg>
      Concierge
    </div>
    <div class="tab active">
      <svg viewBox="0 0 44 44" width="44"><rect x="3" y="4" width="38" height="36" rx="4" fill="none" stroke="currentColor" stroke-width="2.4"/><rect x="3" y="4" width="38" height="8" fill="currentColor"/><g stroke="currentColor" stroke-width="2"><path d="M3 20h38M3 28h38M12 12v28M22 12v28M32 12v28"/></g><g fill="#000"><rect x="11" y="6" width="3" height="4"/><rect x="30" y="6" width="3" height="4"/></g></svg>
      Calendar
    </div>
    <div class="tab">
      <svg viewBox="0 0 44 44" width="44"><g fill="none" stroke="currentColor" stroke-width="2"><circle cx="30" cy="14" r="10"/><circle cx="33" cy="11" r="3"/><path d="M22 21L4 39v3h6v-4h4v-4h4l6-7"/></g></svg>
      Vantor Locks
    </div>
  </nav>
</main>
</body>
</html>
```